Verpackungsdesign für Parfüm gesucht
Zielgruppe
Wir werden eine Marke unter dem Namen ORMAL mit Parfüm auf dem Markt bringen und benötigen hierfür ein hochwertiges Design . Unsre Zielgruppe ist m/w/d und zwischen 16 und 60 Jahre.
Aufgabenstellung
Bei der Verpackung handelt es sich um eine Schiebeschachtel. Wir benötigen das Design nur für die Außenhülle, nicht für den Schuber.
Pflichtangaben auf der Verpackung sind unser Logo, Eau de Parfum, High Intense, 20 ml e 0.67 FL OZ,
Natural Spray Vaporisateur,

```html
<!DOCTYPE html>
<html lang="de">
<head>
<meta charset="utf-8">
<title>ORMAL – Eau de Parfum Faltschachtel</title>
<link rel="stylesheet" href="https://fonts.googleapis.com/css2?family=Jost:wght@300;400&family=Montserrat:wght@400;500&display=swap">
<style>
  :root{
    --stage:#8c8c8c;
    --sleeve:#f7f7f7;
    --ink:#8e8e8e;
    --ink-soft:#a9a9a9;
    --logo:#b4b4b4;
    --fold:#5fe07a;
    --cut:#e38a8a;
    --pattern-a:#f7f7f7;
    --pattern-b:#e4e4e4;
  }
  *{margin:0;padding:0;box-sizing:border-box}
  html,body{width:800px;height:1200px;overflow:hidden;background:var(--stage)}
  .canvas{position:relative;width:800px;height:1200px}
  .dieline{position:absolute;left:29px;top:403px;width:742px;height:393px}
  .flap{position:absolute;left:0;top:0;width:88px;height:393px}
  .panel{position:absolute;top:0;height:393px;background:var(--sleeve);overflow:hidden}
  .spine-left{left:88px;width:64px}
  .front{left:152px;width:262px}
  .spine-right{left:414px;width:66px}
  .back{left:480px;width:262px}
  .fold{position:absolute;top:0;width:1px;height:393px;background:var(--fold)}
  .brand{
    font-family:"Jost",sans-serif;font-weight:300;color:var(--logo);
    letter-spacing:.16em;text-align:center;line-height:1;
  }
  .front .brand{position:absolute;top:55px;left:0;width:100%;font-size:46px;padding-left:.16em}
  .variant{
    position:absolute;top:128px;left:0;width:100%;text-align:center;
    font-family:"Montserrat",sans-serif;font-size:13px;line-height:18px;color:var(--ink);
  }
  .volume{
    position:absolute;top:355px;left:0;width:100%;text-align:center;
    font-family:"Montserrat",sans-serif;font-size:10.5px;color:var(--ink);
  }
  .pattern{
    position:absolute;left:0;right:0;top:190px;bottom:0;
    background:linear-gradient(160deg,var(--pattern-a) 0%,var(--pattern-b) 55%,var(--pattern-a) 100%);
  }
  .spine-text{
    position:absolute;left:50%;white-space:nowrap;
    transform:translate(-50%,-50%) rotate(-90deg);
  }
  .spine-claim{top:150px;font-family:"Montserrat",sans-serif;font-size:12px;color:var(--ink-soft)}
  .spine-brand{top:318px;font-size:28px}
</style>
</head>
<body>
<div class="canvas">
  <div class="dieline">
    <svg class="flap" viewBox="0 0 88 393" aria-hidden="true">
      <polygon points="0,17 88,0 88,393 0,376" fill="#f7f7f7" stroke="#e38a8a" stroke-width="1"/>
    </svg>

    <section class="panel spine-left">
      <span class="spine-text spine-claim">Natural Spray Vaporisateur</span>
      <span class="spine-text brand spine-brand">ORMAL</span>
    </section>

    <section class="panel front">
      <div class="pattern" role="img" aria-label="Feines Muster aus sich kreuzenden hellgrauen Linien"></div>
      <h1 class="brand">ORMAL</h1>
      <p class="variant">Eau de Parfum<br>High Intense</p>
      <p class="volume">ml e 0.67 FL OZ 20</p>
    </section>

    <section class="panel spine-right">
      <span class="spine-text spine-claim">Natural Spray Vaporisateur</span>
      <span class="spine-text brand spine-brand">ORMAL</span>
    </section>

    <section class="panel back">
      <div class="pattern" role="img" aria-label="Feines Muster aus sich kreuzenden hellgrauen Linien"></div>
    </section>

    <span class="fold" style="left:88px"></span>
    <span class="fold" style="left:152px"></span>
    <span class="fold" style="left:414px"></span>
    <span class="fold" style="left:480px"></span>
  </div>
</div>
</body>
</html>
```